Rolf Denning & Martin Oakshaw Two Piano Recital

We need a flyer designed to advertise a classical concert featuring pianists Martin Oakshaw & Rolf Denning playing two pianos.

The concert will be held at Brindlemoor College on Thursday, June 12th at 7:30pm
Supper will be served!
We need something that will get noticed and look cool possibly using the photo attached?

```html
<!DOCTYPE html>
<html lang="en">
<head>
<meta charset="utf-8">
<title>Rolf Denning &amp; Martin Oakshaw – Two Piano Recital</title>
<link href="https://fonts.googleapis.com/css2?family=Open+Sans:wght@400;600&display=swap" rel="stylesheet">
<style>
  :root {
    --paper: #ffffff;
    --ink: #000000;
    --amber: #f5b70f;
    --amber-soft: rgba(245, 183, 15, 0.9);
    --smoke: rgba(40, 40, 40, 0.82);
    --smoke-light: rgba(90, 90, 90, 0.55);
    --photo-light: #d9d9d9;
    --photo-mid: #8a8a8a;
    --photo-dark: #2b2b2b;
  }
  * { margin: 0; padding: 0; box-sizing: border-box; }
  html, body { width: 862px; height: 1200px; overflow: hidden; background: var(--paper); }
  body { font-family: "Open Sans", Arial, sans-serif; }
  .flyer { position: relative; width: 862px; height: 1200px; background: var(--paper); }
  .hero-photo {
    position: absolute; left: 37px; top: 35px; width: 788px; height: 1130px;
    background:
      linear-gradient(90deg, var(--photo-dark) 0%, var(--photo-mid) 12%, var(--photo-dark) 22%, var(--photo-dark) 45%, var(--photo-light) 55%, var(--photo-mid) 70%, var(--photo-dark) 80%, var(--photo-dark) 100%),
      var(--photo-mid);
    background-blend-mode: normal;
  }
  .artwork { position: absolute; left: 0; top: 0; }
  .band-smoke { fill: var(--smoke); }
  .band-smoke-light { fill: var(--smoke-light); }
  .band-amber { fill: var(--amber-soft); }
  .band-ink { fill: var(--ink); }
  .band-amber-solid { fill: var(--amber); }
  .event-kind { font-size: 34px; fill: var(--paper); font-weight: 400; }
  .performer { font-size: 80px; fill: var(--ink); font-weight: 400; }
  .venue { font-size: 20px; fill: var(--paper); font-weight: 400; }
  .date { font-size: 25px; fill: var(--amber); }
  .tickets { font-size: 21px; fill: var(--paper); }
  .bookings { font-size: 21px; fill: var(--ink); }
</style>
</head>
<body>
<div class="flyer">
  <div class="hero-photo" role="img" aria-label="Black and white photo of two men in waistcoats and shirts standing against a wall, cropped at the shoulders"></div>

  <svg class="artwork" width="862" height="1200" viewBox="0 0 862 1200">
    <defs>
      <clipPath id="photo-area"><rect x="37" y="35" width="788" height="1130"/></clipPath>
    </defs>
    <g clip-path="url(#photo-area)">
      <g transform="translate(37 800) rotate(-17.5)">
        <rect class="band-smoke" x="-300" y="-185" width="1400" height="58"/>
        <text class="event-kind" x="456" y="-140">Two Piano Recital</text>

        <rect class="band-amber" x="-300" y="-127" width="1400" height="118"/>
        <rect class="band-amber" x="-300" y="20" width="840" height="115"/>
        <polygon class="band-amber" points="540,20 740,120 540,135"/>
        <text class="performer" x="77" y="-33">Martin Oakshaw &amp;</text>
        <text class="performer" x="41" y="113">Rolf Denning</text>

        <rect class="band-smoke-light" x="-300" y="135" width="1400" height="8"/>
        <rect class="band-smoke" x="-300" y="143" width="1400" height="40"/>
        <text class="venue" x="-45" y="169">Corran Vale Performing Arts Centre, Brindlemoor College, Ashgrove Road, Fenwick</text>
      </g>

      <polygon class="band-ink" points="420,1062 468,1016 825,1016 825,1062"/>
      <text class="date" x="793" y="1050" text-anchor="end">12th June 2014 at 7.30 pm</text>

      <rect class="band-ink" x="37" y="1062" width="788" height="56"/>
      <text class="tickets" x="66" y="1097">Tickets $30 (including glass of champagne) $15 concession/students</text>

      <rect class="band-amber-solid" x="37" y="1118" width="788" height="47"/>
      <text class="bookings" x="60" y="1149">Bookings: www.seatline.com/RDMO</text>
      <circle class="band-ink" cx="449" cy="1142" r="6"/>
      <text class="bookings" x="464" y="1149">Enquiries: 0412555019</text>
    </g>
  </svg>
</div>
</body>
</html>
```